product development company BRVENKO LLC business card

We need a business card design for a company based in Texas called 'BRVENKO LLC'. Our first product is a illuminated portable ice chest that is called ' Pebble Drift coolers'. Pebble drift coolers is trademarked. I would like to have the pebble drift trademark somewhere on the card as well as the BRVENKO LLC name.

Target Market(s)

outdoor industry

Industry/Entity Type

Business

Contact Information for Business Card

i would like to have BRVENKO LLC logo larger than the Pebble drift coolers logo.

Font styles to use
Serif
Sans Serif

```html
<!DOCTYPE html>
<html lang="en">
<head>
<meta charset="utf-8">
<title>BRVENKO LLC – Business Card</title>
<link rel="stylesheet" href="https://fonts.googleapis.com/css2?family=Cinzel:wght@600&family=Open+Sans:wght@400;600;700&display=swap">
<style>
  :root {
    --stage: #4a3428;
    --card-front: #a6a6a6;
    --card-back: #141414;
    --ink-light: #ffffff;
    --shadow: rgba(0,0,0,0.45);
  }
  * { margin: 0; padding: 0; box-sizing: border-box; }
  html, body { width: 1200px; height: 1000px; overflow: hidden; }
  body {
    position: relative;
    background: var(--stage);
    font-family: "Open Sans", Arial, sans-serif;
    color: var(--ink-light);
  }
  .card {
    position: absolute;
    left: 265px;
    width: 666px;
    height: 397px;
    box-shadow: 0 4px 14px var(--shadow);
  }
  .card--front { top: 73px; background: var(--card-front); }
  .card--back { top: 532px; background: var(--card-back); }

  .company-name {
    position: absolute;
    font-family: "Cinzel", Georgia, serif;
    font-weight: 600;
    color: var(--ink-light);
    text-align: center;
    line-height: 1;
  }
  .company-name__main { display: block; }
  .company-name__suffix { display: block; }

  .card--front .company-name { left: 33px; top: 44px; width: 296px; }
  .card--front .company-name__main { font-size: 42px; letter-spacing: 1px; }
  .card--front .company-name__suffix { font-size: 20px; letter-spacing: 10px; margin-top: 6px; padding-left: 10px; }

  .card--back .company-name { left: 0; width: 100%; top: 153px; }
  .card--back .company-name__main { font-size: 52px; letter-spacing: 1px; }
  .card--back .company-name__suffix { font-size: 24px; letter-spacing: 12px; margin-top: 8px; padding-left: 12px; }

  .person { position: absolute; left: 33px; top: 183px; }
  .person__name { font-weight: 700; font-size: 20px; letter-spacing: 0.3px; line-height: 1.1; }
  .person__title { font-size: 15.5px; line-height: 1.4; }

  .contacts { position: absolute; left: 33px; top: 246px; list-style: none; }
  .contacts__item {
    display: flex; align-items: center;
    font-size: 15.5px; height: 23px;
  }
  .contacts__item svg { width: 14px; height: 16px; margin-right: 8px; flex: none; }
  .contacts__item--address { margin-top: 5px; }

  .product-mark {
    position: absolute; right: 32px; top: 262px;
    display: flex; align-items: center; gap: 8px;
    font-family: "Open Sans", Arial, sans-serif;
    font-weight: 600; font-size: 19px; color: var(--ink-light);
  }
  .product-mark__dot { width: 26px; height: 26px; border-radius: 50%; background: var(--ink-light); }
</style>
</head>
<body>
  <section class="card card--front">
    <h1 class="company-name">
      <span class="company-name__main">BRVENKO</span>
      <span class="company-name__suffix">LLC</span>
    </h1>

    <div class="person">
      <p class="person__name">MARCUS ELWOOD</p>
      <p class="person__title">Managing Director</p>
    </div>

    <ul class="contacts">
      <li class="contacts__item">
        <svg viewBox="0 0 14 16" aria-hidden="true"><rect x="3" y="1" width="8" height="14" rx="1.5" fill="none" stroke="#fff" stroke-width="1.4"/><rect x="5" y="3" width="4" height="5" fill="#fff"/></svg>
        + 000 000 0000
      </li>
      <li class="contacts__item">
        <svg viewBox="0 0 14 16" aria-hidden="true"><path d="M1 7 Q7 2 13 7 L11 8.5 L9 7 L5 7 L3 8.5 Z" fill="#fff"/><rect x="3" y="9" width="8" height="4" rx="1" fill="#fff"/></svg>
        + 000 000 0000
      </li>
      <li class="contacts__item">
        <svg viewBox="0 0 14 16" aria-hidden="true"><rect x="1" y="4" width="12" height="8" fill="#fff"/><path d="M1 4 L7 9 L13 4" fill="none" stroke="#a6a6a6" stroke-width="1.2"/></svg>
        info@brvenkopebbledrift.com
      </li>
      <li class="contacts__item">
        <svg viewBox="0 0 14 16" aria-hidden="true"><circle cx="7" cy="8" r="5.5" fill="none" stroke="#fff" stroke-width="1.4"/><path d="M1.5 8 H12.5 M7 2.5 Q3.5 8 7 13.5 M7 2.5 Q10.5 8 7 13.5" fill="none" stroke="#fff" stroke-width="1.1"/></svg>
        www.brvenkopebbledrift.com
      </li>
      <li class="contacts__item contacts__item--address">
        <svg viewBox="0 0 14 16" aria-hidden="true"><path d="M7 15 Q1.5 8.5 1.5 6 A5.5 5.5 0 0 1 12.5 6 Q12.5 8.5 7 15 Z" fill="#fff"/><circle cx="7" cy="6" r="2" fill="#a6a6a6"/></svg>
        1840 W. Mesa Ave. Alton, TX 78573
      </li>
    </ul>

    <div class="product-mark">
      <span class="product-mark__dot" aria-hidden="true"></span>
      <span class="product-mark__name">Pebble Drift coolers</span>
    </div>
  </section>

  <section class="card card--back">
    <h2 class="company-name">
      <span class="company-name__main">BRVENKO</span>
      <span class="company-name__suffix">LLC</span>
    </h2>
  </section>
</body>
</html>
```